Willow Current Mind Studio

I need a brain fitness website that is on the WordPress platform. It needs to feel friendly and relaxing. We are not a physical health gym, but a brain health coaching facility. I can produce hundreds of professional photos. It can be one long page or five short pages.

Industry/Entity Type

Health And Wellness

```html
<!DOCTYPE html>
<html lang="en">
<head>
<meta charset="utf-8">
<title>Willow Current Mind Studio</title>
<link href="https://fonts.googleapis.com/css2?family=Montserrat:wght@400;500;600;700;800&family=Open+Sans:wght@400;600;700&display=swap" rel="stylesheet">
<style>
:root{
  --crimson:#8e0f1f;
  --pink:#e0124f;
  --ink:#2b2b2b;
  --dark:#222222;
  --darker:#1b1b1b;
  --grey:#8a8a8a;
  --light:#d9d9d9;
  --white:#ffffff;
  --blue:#2a9fd8;
}
*{box-sizing:border-box;margin:0;padding:0}
html,body{width:1200px;height:3087px;overflow:hidden}
body{position:relative;background:var(--white);font-family:"Open Sans",Arial,sans-serif;color:var(--ink)}
.abs{position:absolute}

/* header */
.site-header{left:0;top:0;width:1200px;height:99px;background:var(--white)}
.brand{left:86px;top:22px;display:flex;align-items:center;gap:12px}
.brand-dot{width:50px;height:50px;border-radius:50%;background:#e9e3ef}
.brand-name{font-family:"Montserrat",sans-serif;font-weight:600;font-size:21px;color:var(--crimson);letter-spacing:.5px}
.nav{right:86px;top:42px;display:flex;gap:44px;font-family:"Montserrat",sans-serif;font-weight:500;font-size:15px;color:#333}

/* hero */
.hero{left:0;top:99px;width:1200px;height:576px;background:linear-gradient(90deg,#8a1020 0%,#b5233a 35%,#c79a8a 65%,#7d6a66 100%)}
.hero-title{left:99px;top:150px;color:var(--white)}
.hero-title .kicker{font-family:"Montserrat",sans-serif;font-weight:800;font-size:58px;line-height:1}
.hero-title .line{font-family:"Montserrat",sans-serif;font-weight:600;font-size:50px;line-height:57px;margin-top:20px}

/* welcome */
.welcome-title{left:0;top:762px;width:1200px;text-align:center;font-family:"Montserrat",sans-serif;font-weight:600;font-size:37px;color:#333}
.welcome-sub{left:0;top:822px;width:1200px;display:flex;justify-content:center;align-items:center;gap:16px;font-family:"Montserrat",sans-serif;font-size:17px;color:var(--crimson)}
.welcome-sub span.rule{width:130px;height:1px;background:#cfcfcf}

.program{width:500px;height:240px}
.program .thumb{position:absolute;left:0;top:0;width:156px;height:156px;border-radius:50%}
.program .body{position:absolute;left:184px;top:0;width:305px}
.program .level{font-family:"Montserrat",sans-serif;font-weight:700;font-size:12px;color:#222}
.program .name{font-family:"Montserrat",sans-serif;font-weight:600;font-size:17px;color:var(--pink);margin-top:10px}
.program .text{font-size:13px;line-height:23px;color:#777;margin-top:14px}
.program .btn{display:flex;margin-top:20px;height:31px}
.program .btn b{width:138px;background:var(--dark);color:var(--white);font-family:"Montserrat",sans-serif;font-size:11px;font-weight:700;display:flex;align-items:center;justify-content:center}
.program .btn i{width:35px;background:var(--pink);display:flex;align-items:center;justify-content:center}

/* gallery */
.gallery{left:0;top:1486px;width:1200px;height:453px;background:var(--dark)}
.tile{position:absolute}
.schedule{font-family:"Montserrat",sans-serif;color:var(--white);font-size:10px}
.schedule h4{text-align:center;font-size:13px;font-weight:600;margin:24px 0 12px}
.schedule table{margin:0 auto;border-collapse:collapse;width:180px}
.schedule td{padding:5px 0;border-bottom:1px solid rgba(255,255,255,.25)}
.schedule td:last-child{text-align:right}

/* video */
.video-title{left:675px;top:2030px;font-family:"Montserrat",sans-serif;font-weight:500;font-size:35px;color:#333}
.video-lead{left:680px;top:2100px;width:400px;font-size:12px;line-height:21px;font-weight:700;color:var(--crimson)}
.video-text{left:680px;top:2188px;width:400px;font-size:12px;line-height:21px;color:#8d8d8d}
.video-text p+p{margin-top:18px}
.passion{left:680px;top:2418px;font-family:"Montserrat",sans-serif;font-weight:800;font-size:41px;line-height:52px;color:#d8d8d8}
.arrow-btn{width:32px;height:32px;border:1px solid #999;border-radius:50%;display:flex;align-items:center;justify-content:center}

/* footer */
.footer{left:0;top:2690px;width:1200px;height:397px;background:var(--darker)}
.call-band{left:0;top:2675px;width:556px;height:118px}
.call-text{left:0;top:2690px;width:497px;text-align:right;color:var(--white)}
.call-text small{display:block;font-family:"Montserrat",sans-serif;font-size:19px}
.call-text strong{display:block;font-family:"Montserrat",sans-serif;font-size:36px;font-weight:700;margin-top:4px}
.hours-title{left:595px;top:2700px;font-family:"Montserrat",sans-serif;font-size:18px;color:var(--white)}
.hours{top:2740px;color:var(--white);font-family:"Montserrat",sans-serif}
.hours b{display:block;font-size:12px;font-weight:600}
.hours span{display:block;font-size:10.5px;color:#aaa;margin-top:8px}
.hours-rule{left:595px;top:2800px;width:480px;height:1px;background:#3b3b3b}

.col-title{font-family:"Montserrat",sans-serif;font-size:22px;color:var(--white)}
.links{left:99px;top:2900px;font-size:13px;line-height:23px;color:#ddd;list-style:none}
.contact-row{display:flex;gap:12px;align-items:flex-start;color:#ddd;font-size:12px;line-height:16px}
.contact-row i{width:24px;height:24px;border-radius:50%;background:var(--blue);flex:none;display:flex;align-items:center;justify-content:center}
.field{background:#3a3a3a;color:#bbb;font-size:9px;font-family:"Montserrat",sans-serif;padding:9px 8px}
.submit{background:var(--blue);color:var(--white);font-family:"Montserrat",sans-serif;font-weight:600;font-size:12px;display:flex;align-items:center;justify-content:center}
.foot-brand{left:870px;top:2840px;width:224px;text-align:center;color:var(--white)}
.foot-brand .dot{width:70px;height:70px;border-radius:50%;border:1px solid #777;margin:0 auto 14px}
.foot-brand .name{font-family:"Montserrat",sans-serif;font-size:17px;font-weight:500;line-height:22px}
.social{left:906px;top:2968px;display:flex;gap:11px}
.social i{width:27px;height:27px;border-radius:50%;background:#e7e7e7}
.copyright{left:0;top:3058px;width:1200px;text-align:center;font-size:10px;color:#777}
.copy-rule{left:0;top:3045px;width:1200px;height:1px;background:#2e2e2e}
</style>
</head>
<body>

<header class="site-header abs">
  <div class="brand abs"><span class="brand-dot"></span><span class="brand-name">WILLOW CURRENT MIND STUDIO</span></div>
  <nav class="nav abs"><span>HOME</span><span>ABOUT</span><span>CLASSES</span><span>EVENTS</span><span>NEWS</span><span>SHOP</span></nav>
</header>

<section class="hero abs" role="img" aria-label="Photo of a calm woman resting on a blue mat beside a red ball in a warm studio">
  <div class="hero-title abs">
    <div class="kicker">BRAIN FITNESS</div>
    <div class="line">Are You<br>Ready<br>To Change ?</div>
  </div>
</section>

<h2 class="welcome-title abs">WELCOME TO WILLOW CURRENT</h2>
<div class="welcome-sub abs"><span class="rule"></span>MIND STUDIO<span class="rule"></span></div>

<article class="program abs" style="left:86px;top:936px">
  <div class="thumb" role="img" aria-label="Photo of a client in a memory coaching session" style="background:radial-gradient(circle,#cfcfd4,#5a5f6e)"></div>
  <div class="body"><div class="level">Beginner Level</div><div class="name">Memory Basics</div>
  <p class="text">Ne vero choro voluptatum est, an est tale debitis molestiae, nam ei quidam quaestio. Mea in inani cotidieque appellantur, no vix postea phaedrum.</p>
  <div class="btn"><b>VIEW SESSIONS</b><i><svg width="14" height="14" viewBox="0 0 14 14"><circle cx="7" cy="7" r="6" fill="#fff"/><path d="M6 4l3 3-3 3" stroke="#e0124f" stroke-width="1.8" fill="none"/></svg></i></div></div>
</article>
<article class="program abs" style="left:628px;top:936px">
  <div class="thumb" role="img" aria-label="Photo of a woman in a relaxed focus pose on a yellow background" style="background:radial-gradient(circle,#f4d36a,#d4902e)"></div>
  <div class="body"><div class="level">Intermediate Level</div><div class="name">Focus Exercises</div>
  <p class="text">Ne vero choro voluptatum est, an est tale debitis molestiae, nam ei quidam quaestio. Mea in inani cotidieque appellantur, no vix postea phaedrum.</p>
  <div class="btn"><b>VIEW SESSIONS</b><i><svg width="14" height="14" viewBox="0 0 14 14"><circle cx="7" cy="7" r="6" fill="#fff"/><path d="M6 4l3 3-3 3" stroke="#e0124f" stroke-width="1.8" fill="none"/></svg></i></div></div>
</article>
<article class="program abs" style="left:86px;top:1198px">
  <div class="thumb" role="img" aria-label="Photo of a woman in a balance and coordination drill" style="background:radial-gradient(circle,#eeeeee,#9a9a9a)"></div>
  <div class="body"><div class="level">Advanced Level</div><div class="name">Attention Program</div>
  <p class="text">Ne vero choro voluptatum est, an est tale debitis molestiae, nam ei quidam quaestio. Mea in inani cotidieque appellantur, no vix postea phaedrum.</p>
  <div class="btn"><b>VIEW SESSIONS</b><i><svg width="14" height="14" viewBox="0 0 14 14"><circle cx="7" cy="7" r="6" fill="#fff"/><path d="M6 4l3 3-3 3" stroke="#e0124f" stroke-width="1.8" fill="none"/></svg></i></div></div>
</article>
<article class="program abs" style="left:628px;top:1198px">
  <div class="thumb" role="img" aria-label="Illustration of a glowing blue brain on black" style="background:radial-gradient(circle,#2d6fa8,#050b18)"></div>
  <div class="body"><div class="level">Advanced Level</div><div class="name">Neuro Workout</div>
  <p class="text">Ne vero choro voluptatum est, an est tale debitis molestiae, nam ei quidam quaestio. Mea in inani cotidieque appellantur, no vix postea phaedrum.</p>
  <div class="btn"><b>VIEW SESSIONS</b><i><svg width="14" height="14" viewBox="0 0 14 14"><circle cx="7" cy="7" r="6" fill="#fff"/><path d="M6 4l3 3-3 3" stroke="#e0124f" stroke-width="1.8" fill="none"/></svg></i></div></div>
</article>

<section class="gallery abs">
  <div class="tile" role="img" aria-label="Illustration of glowing neurons with the words brain, body, balance" style="left:86px;top:78px;width:482px;height:315px;background:radial-gradient(circle at 40% 40%,#d9782a,#5b3a8e 45%,#101a3c)"></div>
  <div class="tile" role="img" aria-label="Photo of a cheerful group class in the studio" style="left:591px;top:78px;width:251px;height:148px;background:linear-gradient(135deg,#7fc4e8,#e36aa0)"></div>
  <div class="tile schedule" style="left:864px;top:78px;width:251px;height:148px;background:linear-gradient(135deg,#5a2a33,#2e2226)">
    <h4>Mindfulness</h4>
    <table><tr><td>Wednesday</td><td>11:00 - 12:00</td></tr><tr><td>Thursday</td><td>10:00 - 11:00</td></tr><tr><td>Thursday</td><td>12:00 - 13:00</td></tr><tr><td>Friday</td><td>13:00 - 14:00</td></tr></table>
  </div>
  <div class="tile" role="img" aria-label="Photo of a client in the studio beside a red wall" style="left:591px;top:243px;width:251px;height:163px;background:linear-gradient(135deg,#b3262e,#3a3a3a)"></div>
  <div class="tile" role="img" aria-label="Photo of a coach guiding a client through an exercise" style="left:864px;top:243px;width:251px;height:148px;background:linear-gradient(135deg,#8a6a55,#3d3432)"></div>
</section>

<div class="abs" role="img" aria-label="Photo of clients in a coaching session" style="left:86px;top:1996px;width:235px;height:226px;background:linear-gradient(135deg,#b36b52,#4d3a36)"></div>
<div class="abs" role="img" aria-label="Photo of a coach with a clipboard" style="left:350px;top:1996px;width:251px;height:106px;background:linear-gradient(135deg,#e9eef2,#b9c6d1)"></div>
<div class="abs" role="img" aria-label="Photo of a class relaxing together" style="left:86px;top:2346px;width:296px;height:181px;background:linear-gradient(135deg,#dcc7b6,#8e8179)"></div>
<div class="abs" role="img" aria-label="Video still of a pink network-shaped brain on black" style="left:144px;top:2103px;width:457px;height:294px;background:radial-gradient(circle at 50% 45%,#7a2446,#000 65%)">
  <svg class="abs" style="left:192px;top:111px" width="72" height="72" viewBox="0 0 72 72"><circle cx="36" cy="36" r="36" fill="#fff"/><path d="M29 24l20 12-20 12z" fill="#111"/></svg>
</div>
<div class="arrow-btn abs" style="left:514px;top:2496px"><svg width="10" height="10" viewBox="0 0 10 10"><path d="M6.5 1.5L3 5l3.5 3.5" stroke="#777" fill="none" stroke-width="1.4"/></svg></div>
<div class="arrow-btn abs" style="left:568px;top:2496px"><svg width="10" height="10" viewBox="0 0 10 10"><path d="M3.5 1.5L7 5 3.5 8.5" stroke="#777" fill="none" stroke-width="1.4"/></svg></div>

<h2 class="video-title abs">Watch Video Brain Fitness</h2>
<p class="video-lead abs">We have found the best brain exercises from around the world and put them in one library that you can search by days per week, type of program, and much more!</p>
<div class="video-text abs">
  <p>Many sessions accomplish different goals at the same time. For example, a memory session will almost always help build focus at the same time. Choose the goal that is MOST important to you, and the sessions that are shown will be geared more toward your chosen goal.</p>
  <p>A Split Skill Routine means that you work different mental skills on different days. For example, one session might have you work recall and attention on one day, then planning and calm on a different day. This is the most common type of coaching program.</p>
</div>
<div class="passion abs">YOUR SUCCESS IS<br>OUR PASSION</div>

<footer>
  <div class="footer abs"></div>
  <svg class="call-band abs" width="556" height="118" viewBox="0 0 556 118"><polygon points="0,0 556,0 497,118 0,118" fill="#8e0f1f"/></svg>
  <div class="call-text abs"><small>You can call us toll free</small><strong>(888) 555-0142</strong></div>

  <div class="hours-title abs">opening time</div>
  <svg class="abs" style="left:595px;top:2742px" width="44" height="44" viewBox="0 0 44 44"><circle cx="22" cy="22" r="19" fill="none" stroke="#bbb" stroke-width="2.5"/><path d="M22 11v12l7 5" stroke="#bbb" stroke-width="2.5" fill="none"/></svg>
  <div class="hours abs" style="left:663px"><b>Mon - Fri</b><span>6:00 AM - 11:00 AM</span></div>
  <div class="hours abs" style="left:805px"><b>Saturday</b><span>6:00 AM - 11:00 AM</span></div>
  <div class="hours abs" style="left:947px"><b>Sunday</b><span>6:00 AM - 11:00 AM</span></div>
  <div class="hours-rule abs"></div>

  <div class="col-title abs" style="left:99px;top:2850px">Quick Links</div>
  <ul class="links abs"><li>Home</li><li>How it works</li><li>Features</li><li>Pricing</li><li>Contact us</li></ul>

  <div class="col-title abs" style="left:284px;top:2850px">Contact Us</div>
  <div class="contact-row abs" style="left:284px;top:2895px"><i><svg width="10" height="12" viewBox="0 0 10 12"><path d="M5 11S1 6.5 1 4.2a4 4 0 018 0C9 6.5 5 11 5 11z" fill="#fff"/><circle cx="5" cy="4.2" r="1.4" fill="#2a9fd8"/></svg></i><div><b>WILLOW CURRENT</b><br>418 Lantern Grove Avenue<br>Maple Bay, OR. 97001</div></div>
  <div class="contact-row abs" style="left:284px;top:2960px;align-items:center"><i><svg width="12" height="12" viewBox="0 0 12 12"><path d="M3 1l2 3-1.2 1.2a6 6 0 003 3L8 7l3 2-1 2C5 11 1 7 1 2z" fill="#fff"/></svg></i><div>555-019-2284</div></div>
  <div class="contact-row abs" style="left:284px;top:3000px;align-items:center"><i><svg width="12" height="10" viewBox="0 0 12 10"><rect x="1" y="1" width="10" height="8" fill="#fff"/><path d="M1 1l5 4 5-4" stroke="#2a9fd8" fill="none"/></svg></i><div>hello@willowcurrent.example</div></div>

  <div class="col-title abs" style="left:510px;top:2850px">Book a call back</div>
  <div class="field abs" style="left:510px;top:2897px;width:150px;height:30px">NAME</div>
  <div class="field abs" style="left:510px;top:2935px;width:150px;height:30px">PHONE</div>
  <div class="field abs" style="left:673px;top:2897px;width:168px;height:68px">MESSAGE</div>
  <div class="submit abs" style="left:713px;top:2980px;width:128px;height:32px">SUBMIT</div>

  <div class="foot-brand abs"><div class="dot"></div><div class="name">WILLOW CURRENT<br>MIND STUDIO</div></div>
  <div class="social abs"><i></i><i></i><i></i><i></i></div>

  <div class="copy-rule abs"></div>
  <div class="copyright abs">Copyright 2016-2017 Willow Current. All rights reserved.</div>
</footer>

</body>
</html>
```